Outdoor mass notification company needing business card design.

Our company name is Harrowgate Signal Systems Inc located in Amory Mississippi and we sell and maintain "Brantor" Mass Notification Sirens in the US. Outdoor sirens notify people of certain severe dangers such as tornados, severe thunderstorms, flooding, hurricanes and tsunamis. We also serve the oil and gas refining industries to warn of Chemical releases, fires, and lightning alerts.

Contact Information for Business Card

Name, title, cell number, email address

Requirements
Nice to have
• The Brantor logo and also the Mildvane logo.

```html
<!DOCTYPE html>
<html lang="en">
<head>
<meta charset="utf-8">
<title>Harrowgate Signal Systems – Business Card</title>
<link rel="stylesheet" href="https://fonts.googleapis.com/css2?family=Libre+Baskerville:wght@700&family=Lato:wght@400&family=Montserrat:wght@500;700&display=swap">
<style>
  :root {
    --backdrop: #2b2d31;
    --navy: #33536f;
    --ink: #1f3650;
    --paper: #ffffff;
    --muted: #8a8f96;
    --rule: #9aa0a6;
    --ghost: #eef0f2;
  }
  * { box-sizing: border-box; margin: 0; padding: 0; }
  html, body { width: 1200px; height: 952px; overflow: hidden; }
  body {
    background: var(--backdrop);
    display: flex;
    align-items: center;
    justify-content: center;
    gap: 44px;
  }
  .card {
    position: relative;
    width: 520px;
    height: 297px;
    border-radius: 26px;
    overflow: hidden;
  }
  .card--front {
    background: var(--navy);
    display: flex;
    align-items: center;
    justify-content: center;
  }
  .wordmark {
    font-family: "Libre Baskerville", Georgia, serif;
    font-weight: 700;
    text-transform: uppercase;
    text-align: center;
    line-height: 1.2;
  }
  .card--front .wordmark { color: var(--paper); font-size: 30px; }
  .card--back { background: var(--paper); }
  .card--back .wordmark {
    position: absolute;
    left: 36px;
    top: 32px;
    color: var(--ink);
    font-size: 17px;
    text-align: left;
  }
  .ghost-disc {
    position: absolute;
    right: 70px;
    bottom: -60px;
    width: 220px;
    height: 220px;
    border-radius: 50%;
    background: var(--ghost);
  }
  .contact-list {
    position: absolute;
    left: 36px;
    top: 112px;
    list-style: none;
    font-family: "Lato", Arial, sans-serif;
    font-size: 10.5px;
    color: var(--muted);
    line-height: 1.35;
  }
  .contact-list li {
    display: flex;
    align-items: flex-start;
    gap: 8px;
    margin-bottom: 7px;
  }
  .contact-icon {
    flex: none;
    width: 14px;
    height: 14px;
    border-radius: 2px;
    background: var(--ink);
    display: flex;
    align-items: center;
    justify-content: center;
  }
  .person {
    position: absolute;
    right: 36px;
    top: 150px;
    text-align: right;
  }
  .person__name {
    font-family: "Montserrat", Arial, sans-serif;
    font-weight: 500;
    font-size: 15px;
    letter-spacing: 0.5px;
    color: var(--ink);
    text-transform: uppercase;
  }
  .person__name strong { font-weight: 700; }
  .person__title {
    font-family: "Lato", Arial, sans-serif;
    font-size: 11.5px;
    color: var(--muted);
    margin-top: 2px;
  }
  .person__rule {
    width: 56px;
    height: 1px;
    background: var(--rule);
    margin: 8px 0 0 auto;
  }
</style>
</head>
<body>
  <section class="card card--front" aria-label="Card front">
    <div class="wordmark">Harrowgate<br>Signal Systems</div>
  </section>

  <section class="card card--back" aria-label="Card back">
    <div class="ghost-disc" aria-hidden="true"></div>
    <div class="wordmark">Harrowgate<br>Signal Systems</div>

    <ul class="contact-list">
      <li>
        <span class="contact-icon">
          <svg width="9" height="9" viewBox="0 0 10 10"><path d="M5 0.5a3.2 3.2 0 0 0-3.2 3.2C1.8 6 5 9.5 5 9.5S8.2 6 8.2 3.7A3.2 3.2 0 0 0 5 0.5z" fill="#fff"/><circle cx="5" cy="3.7" r="1.2" fill="#1f3650"/></svg>
        </span>
        <span>2140 Larkspur Avenue<br>Amory, MS 38821</span>
      </li>
      <li>
        <span class="contact-icon">
          <svg width="9" height="9" viewBox="0 0 10 10"><path d="M2.2 0.8l1.6 2-0.9 1.2c0.6 1.2 1.6 2.2 2.8 2.8l1.2-0.9 2 1.6-0.8 1.6C5 9 1 5 0.8 1.6z" fill="#fff"/></svg>
        </span>
        <span>+00 987 654 32</span>
      </li>
      <li>
        <span class="contact-icon">
          <svg width="9" height="9" viewBox="0 0 10 10"><rect x="0.8" y="2" width="8.4" height="6" fill="none" stroke="#fff" stroke-width="1"/><path d="M0.8 2L5 5.5 9.2 2" fill="none" stroke="#fff" stroke-width="1"/></svg>
        </span>
        <span>office@harrowgatesignal.com</span>
      </li>
      <li>
        <span class="contact-icon">
          <svg width="9" height="9" viewBox="0 0 10 10"><path d="M2 1l6 4-2.6 0.5 1.6 3-1.1 0.6-1.6-3L2.5 8z" fill="#fff"/></svg>
        </span>
        <span>www.harrowgatesignal.com</span>
      </li>
    </ul>

    <div class="person">
      <div class="person__name">Daniel R. <strong>Whitford</strong></div>
      <div class="person__title">Managing Director</div>
      <div class="person__rule"></div>
    </div>
  </section>
</body>
</html>
```